Vornel Technologies business card design

We need a business card designed with our new logo. it would be great if the card could communicate it is a technology based company.

Target Market(s)

system integrators

Industry/Entity Type

technology, IOT

Contact Information for Business Card

Name, designation, Address, telephone number, email address

Requirements
Must have
• logo and company name
Nice to have
• something to do with technology

```html
<!DOCTYPE html>
<html lang="en">
<head>
<meta charset="UTF-8">
<title>Vornel Technologies — Business Card</title>
<link rel="stylesheet" href="https://fonts.googleapis.com/css2?family=Lato:wght@400;700&display=swap">
<style>
  :root {
    --page: #e8e5e1;
    --card-white: #ffffff;
    --charcoal: #3e3e40;
    --orange: #f7941d;
    --text-dark: #3a3a3c;
    --text-body: #4a4a4c;
  }
  html, body {
    margin: 0;
    padding: 0;
    width: 1200px;
    height: 1200px;
    overflow: hidden;
    background: var(--page);
    font-family: "Lato", Arial, sans-serif;
  }
  .canvas {
    position: relative;
    width: 1200px;
    height: 1200px;
  }
  .card {
    position: absolute;
    left: 239px;
    width: 722px;
    height: 412px;
    border-radius: 20px;
    overflow: hidden;
    box-shadow: 0 6px 14px rgba(0,0,0,0.18);
  }
  .card-front { top: 140px; background: var(--card-white); }
  .card-back  { top: 645px; background: var(--charcoal); }

  .edge-band {
    position: absolute;
    top: 0;
    right: 0;
    width: 78px;
    height: 100%;
    background: var(--charcoal);
  }
  .edge-accent {
    position: absolute;
    top: 0;
    right: 78px;
    width: 12px;
    height: 100%;
    background: var(--orange);
  }

  .brand {
    position: absolute;
    display: flex;
    align-items: center;
    gap: 12px;
    font-weight: 700;
  }
  .brand-mark {
    width: 32px;
    height: 32px;
    background: var(--orange);
  }
  .brand-name {
    display: flex;
    flex-direction: column;
    line-height: 1;
  }
  .brand-word { letter-spacing: 0.5px; }
  .brand-sub { letter-spacing: 5px; margin-top: 6px; }

  .card-front .brand { left: 42px; top: 44px; color: var(--text-dark); }
  .card-front .brand-word { font-size: 44px; }
  .card-front .brand-sub { font-size: 13px; letter-spacing: 6px; }

  .card-back .brand {
    left: 50%;
    top: 50%;
    transform: translate(-50%, -50%);
    color: #ffffff;
    gap: 18px;
  }
  .card-back .brand-mark { width: 50px; height: 50px; }
  .card-back .brand-word { font-size: 66px; }
  .card-back .brand-sub { font-size: 20px; letter-spacing: 9px; margin-top: 8px; }

  .person {
    position: absolute;
    left: 40px;
    top: 168px;
  }
  .person-name {
    margin: 0;
    font-size: 44px;
    font-weight: 700;
    color: var(--text-dark);
    line-height: 1;
    letter-spacing: -0.3px;
  }
  .person-role {
    margin: 4px 0 0;
    font-size: 23px;
    font-weight: 400;
    color: var(--orange);
  }

  .contact-list {
    position: absolute;
    left: 40px;
    top: 272px;
    margin: 0;
    padding: 0;
    list-style: none;
  }
  .contact-item {
    display: flex;
    align-items: center;
    height: 32px;
    font-size: 19px;
    color: var(--text-body);
  }
  .contact-icon {
    width: 16px;
    height: 16px;
    margin-right: 12px;
    fill: var(--orange);
    flex: none;
  }
</style>
</head>
<body>
<main class="canvas">

  <section class="card card-front" aria-label="Business card front">
    <div class="edge-accent"></div>
    <div class="edge-band"></div>

    <div class="brand">
      <span class="brand-mark"></span>
      <span class="brand-name">
        <span class="brand-word">VORNEL</span>
        <span class="brand-sub">TECHNOLOGIES</span>
      </span>
    </div>

    <div class="person">
      <h1 class="person-name">Your Name Here</h1>
      <p class="person-role">Designation</p>
    </div>

    <ul class="contact-list">
      <li class="contact-item">
        <svg class="contact-icon" viewBox="0 0 24 24" aria-hidden="true"><path d="M6.6 10.8a15.2 15.2 0 0 0 6.6 6.6l2.2-2.2a1 1 0 0 1 1-.25 11.4 11.4 0 0 0 3.6.57 1 1 0 0 1 1 1V20a1 1 0 0 1-1 1A17 17 0 0 1 3 4a1 1 0 0 1 1-1h3.5a1 1 0 0 1 1 1c0 1.25.2 2.45.57 3.57a1 1 0 0 1-.25 1z"/></svg>
        (000) 123-4567
      </li>
      <li class="contact-item">
        <svg class="contact-icon" viewBox="0 0 24 24" aria-hidden="true"><path d="M2 5h20v14H2z"/><path d="M2 5l10 8 10-8" fill="none" stroke="#fff" stroke-width="2"/></svg>
        youre@email.com
      </li>
      <li class="contact-item">
        <svg class="contact-icon" viewBox="0 0 24 24" aria-hidden="true"><path d="M12 2a7 7 0 0 0-7 7c0 5.2 7 13 7 13s7-7.8 7-13a7 7 0 0 0-7-7zm0 9.5A2.5 2.5 0 1 1 12 6.5a2.5 2.5 0 0 1 0 5z"/></svg>
        123 NW Somewhere St., Somewhere City, 1111
      </li>
    </ul>
  </section>

  <section class="card card-back" aria-label="Business card back">
    <div class="brand">
      <span class="brand-mark"></span>
      <span class="brand-name">
        <span class="brand-word">VORNEL</span>
        <span class="brand-sub">TECHNOLOGIES</span>
      </span>
    </div>
  </section>

</main>
</body>
</html>
```